Business card design needed

We are a smash repair business and have been in operation for almost 10 years. We have always had a card with a solid yellow background and black car door as a logo. We don't want to stray too far from this as all of our advertising incorporates same.

We do not wish to have anything comical or too wordy.

Industry/Entity Type

Advertising

Contact Information for Business Card

Rhys & Gemma Tolland
Brookvale Ridge Panel Works
Bays 7-11 Wexford Crescent
Kelsworth NSW 2458
02 6571 3820
0428 362 057
office@brookvaleridgepanelworks.com.au

Logo Text

Brookvale Ridge Panel Works

Logo styles of interest
Emblem Logo

```html
<!DOCTYPE html>
<html lang="en">
<head>
<meta charset="utf-8">
<title>Brookvale Ridge Panel Works – Business Card</title>
<link rel="stylesheet" href="https://fonts.googleapis.com/css2?family=Jost:wght@300;400&display=swap">
<style>
  :root {
    --card-yellow: #ffed00;
    --ink: #1d1d1b;
    --rule: #3a3a30;
  }
  * { margin: 0; padding: 0; box-sizing: border-box; }
  html, body {
    width: 1200px;
    height: 693px;
    overflow: hidden;
    background: var(--card-yellow);
  }
  .card {
    position: relative;
    width: 1200px;
    height: 693px;
    background: var(--card-yellow);
    color: var(--ink);
    font-family: "Jost", sans-serif;
    font-weight: 300;
  }
  .brand-disc {
    position: absolute;
    left: 25px;
    top: 28px;
    width: 260px;
    height: 260px;
  }
  .brand-name {
    position: absolute;
    left: 294px;
    top: 193px;
    font-weight: 300;
    color: var(--ink);
    white-space: nowrap;
  }
  .brand-name .family {
    display: block;
    font-size: 45px;
    line-height: 45px;
    letter-spacing: 0.02em;
  }
  .brand-name .business {
    display: block;
    margin-top: 15px;
    font-size: 25px;
    line-height: 25px;
    letter-spacing: 0.1em;
  }
  .address {
    position: absolute;
    left: 295px;
    top: 316px;
    font-style: normal;
    font-size: 35px;
    line-height: 47px;
    letter-spacing: 0.14em;
    white-space: nowrap;
  }
  .divider {
    position: absolute;
    left: 295px;
    top: 531px;
    width: 879px;
    height: 0;
    border-top: 1.5px solid var(--rule);
  }
  .contact {
    position: absolute;
    left: 295px;
    font-size: 35px;
    line-height: 35px;
    white-space: nowrap;
  }
  .contact-email { top: 558px; letter-spacing: 0.15em; }
  .contact-phone { top: 624px; letter-spacing: 0.155em; }
</style>
</head>
<body>
  <main class="card">
    <svg class="brand-disc" viewBox="0 0 260 260" aria-hidden="true">
      <circle cx="130" cy="130" r="130" fill="var(--ink)"/>
    </svg>

    <div class="brand-name">
      <span class="family">Tolland</span>
      <span class="business">Brookvale Ridge Panel Works Bays</span>
    </div>

    <address class="address">
      Rhys &amp; Gemma Tolland<br>
      Brookvale Ridge Panel Works Bays<br>
      7-11 Wexford Crescent<br>
      Kelsworth NSW 2458 radation
    </address>

    <div class="divider"></div>

    <p class="contact contact-email">E: office@brookvaleridgepanelworks.com.au</p>
    <p class="contact contact-phone">T: 02 6571 3820 0428 362 057</p>
  </main>
</body>
</html>
```